Keelrock Data Partners (KDP) Business Card Design

I would like to create double-sided business cards that contain:
1) Name: Marcus Tolliver
2) Phone Number: +1 (555) 018-2947
3) Email: Marcus.Tolliver@KeelrockDataPartners.com
4) Website: KeelrockDataPartners.com

I would like to include my logo and a color scheme similar to the Vantorra Grand Prix Kelvex team color scheme (black, silver, greenish-blue – but can also include regular blue)

Logos attached.

What we do: Our company develops and delivers innovative and pragmatic information technology and cybersecurity risk and compliance solutions for organizations in the commercial market as well as the federal, and state/local sectors.

```html
<!DOCTYPE html>
<html lang="en">
<head>
<meta charset="utf-8">
<title>Keelrock Data Partners — Business Card</title>
<link href="https://fonts.googleapis.com/css2?family=Michroma&family=Orbitron:wght@700;800&family=Open+Sans:wght@400&display=swap" rel="stylesheet">
<style>
  :root {
    --page-bg: #e9ebec;
    --teal-light: #2aa7a0;
    --teal-dark: #17716f;
    --navy: #0c1428;
    --navy-deep: #05080f;
    --accent-teal: #2bb3b1;
    --accent-blue: #1b6fb8;
    --white: #ffffff;
    --contact-text: #e6eaf0;
  }
  * { margin: 0; padding: 0; box-sizing: border-box; }
  html, body {
    width: 1200px; height: 900px; overflow: hidden;
    background: var(--page-bg);
  }
  .sheet {
    position: relative; width: 1200px; height: 900px;
    display: flex; flex-direction: column; align-items: center; justify-content: center; gap: 40px;
  }
  .card {
    position: relative; width: 700px; height: 400px;
    border-radius: 34px; overflow: hidden;
    box-shadow: 0 10px 28px rgba(0,0,0,0.22);
  }
  .card-front {
    background: radial-gradient(ellipse at 35% 70%, var(--teal-light) 0%, var(--teal-dark) 85%);
  }
  .card-back {
    background: linear-gradient(160deg, var(--navy) 0%, var(--navy-deep) 100%);
  }

  .wordmark {
    position: absolute; display: flex; align-items: center; gap: 18px;
  }
  .wordmark-dot {
    width: 74px; height: 74px; border-radius: 50%;
    border: 6px solid var(--white);
  }
  .wordmark-divider { width: 1.5px; height: 96px; background: var(--white); opacity: 0.85; }
  .wordmark-name {
    font-family: "Michroma", sans-serif; font-size: 27px; line-height: 1.12;
    color: var(--white); letter-spacing: 1px; text-transform: uppercase;
  }
  .card-front .wordmark { left: 150px; top: 170px; }

  .holder-name {
    position: absolute; left: 44px; top: 92px;
    font-family: "Orbitron", sans-serif; font-weight: 800; font-size: 24px;
    letter-spacing: 2px; color: var(--accent-teal); text-transform: uppercase;
  }
  .contact-list {
    position: absolute; left: 340px; top: 150px; list-style: none;
    font-family: "Open Sans", sans-serif; font-size: 13.5px; color: var(--contact-text);
  }
  .contact-list li { display: flex; align-items: center; gap: 9px; height: 24px; }
  .contact-icon { width: 13px; height: 13px; flex: none; }
  .contact-rule {
    position: absolute; left: 340px; top: 232px; width: 330px; height: 1.5px;
    background: linear-gradient(90deg, var(--accent-blue), var(--accent-teal));
  }
  .card-back .wordmark { left: 372px; top: 248px; gap: 14px; }
  .card-back .wordmark-dot { width: 62px; height: 62px; border-color: var(--accent-blue); border-width: 5px; }
  .card-back .wordmark-divider { height: 82px; }
  .card-back .wordmark-name { font-size: 22px; }
</style>
</head>
<body>
<main class="sheet">
  <section class="card card-front" aria-label="Card front">
    <div class="wordmark">
      <span class="wordmark-dot"></span>
      <span class="wordmark-divider"></span>
      <span class="wordmark-name">Keelrock<br>Data<br>Partners</span>
    </div>
  </section>

  <section class="card card-back" aria-label="Card back">
    <h1 class="holder-name">Marcus Tolliver</h1>
    <ul class="contact-list">
      <li>
        <svg class="contact-icon" viewBox="0 0 16 16"><path d="M3 1.5l3 3-1.6 1.8a9 9 0 0 0 5.3 5.3L11.5 10l3 3-2 2C6.5 15 1 9.5 1 3.5z" fill="var(--accent-teal)"/></svg>
        +1 (555) 018-2947
      </li>
      <li>
        <svg class="contact-icon" viewBox="0 0 16 16"><circle cx="8" cy="8" r="6.5" fill="none" stroke="var(--accent-teal)" stroke-width="1.8"/><path d="M1.5 8h13M8 1.5c3 3.5 3 9.5 0 13M8 1.5c-3 3.5-3 9.5 0 13" fill="none" stroke="var(--accent-teal)" stroke-width="1.2"/></svg>
        KeelrockDataPartners.com
      </li>
      <li>
        <svg class="contact-icon" viewBox="0 0 16 16"><rect x="1" y="3" width="14" height="10" rx="1.5" fill="var(--accent-teal)"/><path d="M1.5 4l6.5 5 6.5-5" fill="none" stroke="var(--navy)" stroke-width="1.4"/></svg>
        Marcus.Tolliver@KeelrockDataPartners.com
      </li>
    </ul>
    <div class="contact-rule"></div>
    <div class="wordmark">
      <span class="wordmark-dot"></span>
      <span class="wordmark-divider"></span>
      <span class="wordmark-name">Keelrock<br>Data<br>Partners</span>
    </div>
  </section>
</main>
</body>
</html>
```